Flyer Chorkonzert Best Of Klangfinken
Zielgruppe
Wir sind ein gemischter Chor aus der Schweiz unsere Mitglieder sind zwischen 20 und 70 Jahre jung und singen Querbeet durch die Musik von Lorn bis Tavern.
Weitere Infos www.klangfinken.ch
Aufgabenstellung
Für unser Konzert mit dem Titel " Best Of Klangfinken" brauchen wir für den Flyer ein Vorderseite Design. Das Konzertprogramm beinhaltet folgende Lieder:
Evermoor/ Darby, Bretonischer Mohn / Olaf Brems, Tu dopo noi/ Lukas,Ines+Tobi, Gaderwald / Fluk,Under the lantern/ Gaukler von Ix, Anyone to hold/Tavern, Falling of the tide/ trad. Irl.,Danse ma plume/trad CH,Can't make the tide turn away from us/ Brent Maddox, Alba del sur/Ferndusk, Release my Spirit/Ray Wilder.
Idealerweise nimmt das Design Bezug auf den Titel oder auf eines oder mehrere Lieder.
Format: A5 hoch
Text: "Best of Klangfinken"
Samstag 7. November 2015
17.00 Uhr, Singsaal Halderbühl, Ebnatrain / Seelingen
Sonntag 8. November 2015
17.00 Uhr Grünauersaal, Lindtal am See
Eintritt frei Kollekte

```html
<!DOCTYPE html>
<html lang="de">
<head>
<meta charset="utf-8">
<title>Best Of Klangfinken – Flyer</title>
<link href="https://fonts.googleapis.com/css2?family=Fira+Sans:ital,wght@0,400;0,700;1,700&display=swap" rel="stylesheet">
<style>
  :root {
    --page-bg: #f2f2f2;
    --peach-top: #ffc98a;
    --peach-bottom: #ffc294;
    --program-top: #c98a66;
    --program-mid: #d0694f;
    --program-bottom: #c24a5a;
    --band-left: #ff4a58;
    --band-right: #ff3a6e;
    --lens-fill: #f3a2c0;
    --lens-rim: #ff6c84;
    --text-light: #ffffff;
    --text-soft: #fff3ef;
  }
  * { margin: 0; padding: 0; box-sizing: border-box; }
  html, body { width: 1200px; height: 675px; overflow: hidden; }
  body {
    background: var(--page-bg);
    font-family: "Fira Sans", sans-serif;
    color: var(--text-light);
  }
  .flyer {
    position: absolute;
    left: 377px;
    top: 20px;
    width: 446px;
    height: 634px;
    overflow: hidden;
    box-shadow: 0 6px 18px rgba(0,0,0,.18);
  }
  .flyer-header {
    position: absolute;
    inset: 0 0 auto 0;
    height: 139px;
    background: linear-gradient(180deg, var(--peach-top), var(--peach-bottom));
    display: flex;
    align-items: center;
    justify-content: center;
    gap: 12px;
    box-shadow: 0 3px 6px rgba(0,0,0,.25);
    z-index: 2;
  }
  .brand-mark {
    width: 14px;
    height: 14px;
    background: var(--text-light);
  }
  .brand-name {
    font-weight: 700;
    font-size: 34px;
    letter-spacing: 1px;
    color: var(--text-light);
  }
  .choir-photo {
    position: absolute;
    left: 0; right: 0;
    top: 139px;
    height: 356px;
    background: linear-gradient(180deg, var(--program-top) 0%, var(--program-mid) 55%, var(--program-bottom) 100%);
  }
  .program {
    position: absolute;
    left: 0; right: 0;
    top: 172px;
    text-align: center;
    z-index: 1;
  }
  .program-title {
    font-style: italic;
    font-weight: 700;
    font-size: 15px;
    letter-spacing: .5px;
    margin-bottom: 4px;
  }
  .program-list { list-style: none; }
  .program-list li {
    font-size: 11.5px;
    line-height: 22px;
    letter-spacing: .3px;
    color: var(--text-soft);
  }
  .info-band {
    position: absolute;
    left: 0; right: 0;
    top: 495px;
    bottom: 0;
    background: linear-gradient(90deg, var(--band-left), var(--band-right));
  }
  .entry-lens {
    position: absolute;
    left: 81px;
    top: 455px;
    width: 284px;
    height: 81px;
    z-index: 2;
  }
  .entry-text {
    position: absolute;
    left: 81px;
    top: 478px;
    width: 284px;
    text-align: center;
    z-index: 3;
    line-height: 19px;
  }
  .entry-free { font-size: 14px; letter-spacing: .5px; }
  .entry-collect { font-size: 14px; font-weight: 700; letter-spacing: .5px; }
  .dates {
    position: absolute;
    left: 0; right: 0;
    top: 546px;
    text-align: center;
    z-index: 2;
  }
  .date-day {
    font-weight: 700;
    font-size: 13.5px;
    font-variant: small-caps;
    letter-spacing: .6px;
    line-height: 17px;
  }
  .date-venue {
    font-size: 9.5px;
    letter-spacing: .3px;
    line-height: 13px;
  }
  .date-divider {
    width: 270px;
    height: 1px;
    margin: 6px auto 5px;
    background: rgba(255,255,255,.85);
  }
</style>
</head>
<body>
  <article class="flyer">
    <header class="flyer-header">
      <span class="brand-mark"></span>
      <span class="brand-name">BEST OF KLANGFINKEN</span>
    </header>

    <div class="choir-photo" role="img" aria-label="Chorfoto der Klangfinken, warm orange-rot eingefärbt"></div>

    <section class="program">
      <h2 class="program-title">Konzertprogramm:</h2>
      <ul class="program-list">
        <li>Evermoor/ Darby,</li>
        <li>Bretonischer Mohn / Olaf Brems,</li>
        <li>Tu dopo noi/ Lukas,Ines+Tobi,</li>
        <li>Gaderwald / Fluk,</li>
        <li>Under the lantern/ Gaukler von Ix,</li>
        <li>Anyone to hold/Tavern,</li>
        <li>Falling of the tide/ trad. Irl.,</li>
        <li>Danse ma plume/trad CH,</li>
        <li>Can't make the tide turn away from us/ Brent Maddox,</li>
        <li>Alba del sur/Ferndusk,</li>
        <li>Release my Spirit/Ray Wilder</li>
      </ul>
    </section>

    <div class="info-band"></div>

    <svg class="entry-lens" viewBox="0 0 284 81" aria-hidden="true">
      <defs>
        <radialGradient id="lensGlow" cx="50%" cy="55%" r="60%">
          <stop offset="0" stop-color="#fbc6d8"/>
          <stop offset="1" stop-color="#ea8aae"/>
        </radialGradient>
      </defs>
      <path d="M4 40.5 Q142 -38 280 40.5 Q142 119 4 40.5 Z" fill="url(#lensGlow)" stroke="var(--lens-rim)" stroke-width="3"/>
      <path d="M10 40.5 Q142 -30 274 40.5" fill="none" stroke="rgba(255,255,255,.5)" stroke-width="1"/>
    </svg>
    <div class="entry-text">
      <div class="entry-free">EINTRITT FREI</div>
      <div class="entry-collect">KOLLEKTE</div>
    </div>

    <section class="dates">
      <div class="date-day">Samstag 7. November 2015</div>
      <div class="date-venue">17.00 Uhr, Singsaal Halderbühl, Ebnatrain / Seelingen</div>
      <div class="date-divider"></div>
      <div class="date-day">Sonntag 8. November 2015</div>
      <div class="date-venue">17.00 Uhr Grünauersaal, Lindtal am See</div>
    </section>
  </article>
</body>
</html>
```